依頼詳細
現状はデザインの入ったアルミパックとなっておりますが、今回デザインした箱に無地のアルミパックを入れる方向に転換したいと思っておりますので、箱のデザインを依頼したいと思います。しかしながら、アルミパックのままデザインのみ変更する場合も考えられますので、どちらでも使えるデザインだと大変助かります。
記載項目
現状サイズ:たて約23cm×よこ約17cmのパック。
希望イメージ
シンプル 複雑
単色 カラフル
暗い 明るい
日常 高級
遊び心 厳粛
未来的 伝統的
女性的 男性的
希望する色
納品ファイル
• 高解像度JPG (.jpg)
• イラストレーター形式 (.ai)
補足説明
添付は現在の商品デザインになります。
皆様ご提案頂き誠にありがとうございます。
延長の理由を追記させて頂きます。
当方のイメージとしましては、全体的にもう少し「アート感」が欲しいところであります。
香川県はうどんだけでなく、直島などのアートの県としての特徴もございますので、その辺りを含んだデザインでお願い致します。
■ 選んだ理由

皆様たくさんのご提案誠にありがとうございました。
とても良いデザインが多いなか選考に時間がかかりましたが、個人的にパッと見たときのデザイン性、斬新さなどからこちらのデザインに決定させて頂きました。和をイメージして頂いたデザインも多かったですが、よくある和なイメージかなと思いましたのと、四国をイメージして頂いていたものも海外の方には分かりにくいかなと思い、今回のちょっと違った捉え方をした「和」とデザイン性(アート)の感じられたこちらのデザインに決定させて頂きました。皆様ご提案ありがとうございました。

■ 提案者全員のお礼・コメント

改めましてこの度は素晴らしいデザインのご提案、誠にありがとうございました。また早速コメントも返信頂きありがとうございます。後ほど一部修正案等まとめまして、ご相談させて頂きます。引き続きどうぞよろしくお願い致します。

```html
<!DOCTYPE html>
<html lang="ja">
<head>
<meta charset="utf-8">
<title>凪と椀 だしパック</title>
<link rel="stylesheet" href="https://fonts.googleapis.com/css2?family=Shippori+Mincho:wght@500;700;800&family=Cormorant+Garamond:ital,wght@0,500;1,500&display=swap">
<style>
  :root {
    --paper: #e9e8e6;
    --band: #fbfbfa;
    --band-edge: #d2d1cf;
    --ink: #2f2f2f;
    --green: #3f7a3a;
    --pine: #8db552;
    --sand: #c7b79a;
    --sea: #6b94c6;
    --blossom: #d86aa7;
    --coral: #e27560;
    --teal: #4ea8b0;
  }
  html, body { margin: 0; padding: 0; overflow: hidden; }
  body { width: 888px; height: 1200px; background: var(--paper); }
  .package {
    position: relative; width: 888px; height: 1200px; overflow: hidden;
    background: radial-gradient(circle at 30% 20%, #f1f0ee, var(--paper) 70%);
  }
  .center-band {
    position: absolute; left: 308px; top: 0; width: 266px; height: 1200px;
    background: var(--band);
    border-left: 3px solid var(--band-edge);
    border-right: 3px solid var(--band-edge);
  }
  .emblem { position: absolute; border-radius: 50%; width: 188px; height: 188px; }
  .emblem--pine    { left: 44px;  top: 118px; background: var(--pine); }
  .emblem--sand    { left: 660px; top: 118px; background: var(--sand); }
  .emblem--sea     { left: 44px;  top: 415px; background: var(--sea); }
  .emblem--blossom { left: 660px; top: 425px; background: var(--blossom); }
  .emblem--coral   { left: 56px;  top: 690px; width: 168px; height: 168px; background: var(--coral); }
  .emblem--teal    { left: 666px; top: 640px; width: 168px; height: 168px; background: var(--teal); }

  .tagline {
    position: absolute; top: 26px; left: 0; width: 888px; text-align: center;
    font-family: "Shippori Mincho", serif; font-weight: 700; font-size: 34px;
    color: var(--ink); letter-spacing: 1px; line-height: 1.4;
  }
  .subtitle {
    position: absolute; top: 112px; left: 0; width: 888px; text-align: center;
    font-family: "Cormorant Garamond", serif; font-weight: 500; font-size: 32px;
    color: var(--green); line-height: 1.2;
  }
  .product-name-group { margin: 0; }
  .product-name {
    position: absolute; left: 0; width: 888px; text-align: center;
    font-family: "Shippori Mincho", serif; font-weight: 800; color: var(--green); line-height: 1;
  }
  .product-name--first { top: 160px; font-size: 185px; }
  .product-name--mid   { top: 355px; font-size: 80px; }
  .product-name--last  { top: 448px; font-size: 185px; }
  .reading {
    position: absolute; left: 286px; top: 410px;
    writing-mode: vertical-rl;
    font-family: "Shippori Mincho", serif; font-size: 16px; color: var(--ink);
    letter-spacing: 3px;
  }
  .portion {
    position: absolute; top: 680px; left: 0; width: 888px; text-align: center;
    font-family: "Shippori Mincho", serif; font-weight: 500; font-size: 30px;
    color: var(--ink); line-height: 1.3;
  }
  .copy {
    position: absolute; top: 778px; left: 0; width: 888px; text-align: center;
    font-family: "Shippori Mincho", serif; font-weight: 700; font-size: 21px;
    line-height: 1.65; color: var(--ink); margin: 0;
  }
  .latin-name {
    position: absolute; left: 0; width: 888px; text-align: center;
    font-family: "Cormorant Garamond", serif; font-weight: 500; color: var(--green);
    letter-spacing: 6px; line-height: 1; font-size: 72px;
  }
  .latin-name--first { top: 952px; }
  .latin-name--last  { top: 1040px; }
</style>
</head>
<body>
<main class="package">
  <div class="center-band"></div>

  <div class="emblem emblem--pine" role="img" aria-label="円形の紋:松の意匠"></div>
  <div class="emblem emblem--sand" role="img" aria-label="円形の紋:波の意匠"></div>
  <div class="emblem emblem--sea" role="img" aria-label="円形の紋:渦巻く波の意匠"></div>
  <div class="emblem emblem--blossom" role="img" aria-label="円形の紋:波しぶきの意匠"></div>
  <div class="emblem emblem--coral" role="img" aria-label="円形の紋:山並みと波の意匠"></div>
  <div class="emblem emblem--teal" role="img" aria-label="円形の紋:渦の意匠"></div>

  <div class="tagline">料亭仕込み【だしパック】</div>
  <div class="subtitle">Dashi Pack</div>

  <h1 class="product-name-group" aria-label="凪と椀">
    <span class="product-name product-name--first" aria-hidden="true">凪</span>
    <span class="product-name product-name--mid" aria-hidden="true">と</span>
    <span class="product-name product-name--last" aria-hidden="true">椀</span>
  </h1>
  <div class="reading">なぎとわん</div>

  <div class="portion">4人前×20袋</div>
  <p class="copy">プロの味をご家庭に・・・<br>すべて国産天然素材に<br>こだわりを持って仕上げました。</p>

  <div class="latin-name latin-name--first">NAGI TO</div>
  <div class="latin-name latin-name--last">WAN</div>
</main>
</body>
</html>
```